website design for a new age Real Estate Security Business

We are launching a business in real estate which no body else is doing. We are going to use technology in terms of software and hardware to provide our services.

We are going to use Big Data, IOT etc.. for our services.

NOTE: We don't want to see Shiel or buildings etc.. that directly suggests Real estate or security on this design

Target Market(s)

India

Industry/Entity Type

Real Estate

Number of Pages Required

4 page

Font styles to use
Sans Serif
Other font styles liked:
• Use Google Fonts

Requirements
Must have
• Home Page should be trendy and colourful should give user confidence to subscribe to our service.
Nice to have
• Use Google fonts.
Should not have
• Design shouldnt have Shield or Buildings that directly suggests real estate or security.

```html
<!DOCTYPE html>
<html lang="en">
<head>
<meta charset="utf-8">
<title>Property Safe — Data, Analysis, Action</title>
<link rel="stylesheet" href="https://fonts.googleapis.com/css2?family=Lato:wght@400;700&family=Roboto:wght@400;500;700&display=swap">
<style>
:root{
  --accent:#f2493a;
  --ink:#2a2a2e;
  --text:#4a4a50;
  --muted:#6b6b72;
  --line:#e4e4e8;
  --standard:#d04b7b;
  --standard-dark:#a8365e;
  --extended:#3fb0c6;
  --extended-dark:#2a8ea3;
  --premium:#5db59b;
  --premium-dark:#3f9479;
  --ribbon:#f7a11a;
  --footer:#1e1f24;
  --white:#ffffff;
}
*{margin:0;padding:0;box-sizing:border-box}
html,body{width:1200px;height:2419px;overflow:hidden;background:var(--white)}
body{position:relative;font-family:'Roboto',Arial,sans-serif;color:var(--text)}

/* header */
.site-header{position:absolute;left:0;top:0;width:1200px;height:68px;background:var(--white);z-index:5}
.brand{position:absolute;font-family:'Roboto',Arial,sans-serif;font-weight:700;font-size:21px;color:var(--ink);line-height:26px}
.site-header .brand{left:89px;top:21px}
.nav{position:absolute;display:flex;font-size:13px;color:var(--muted)}
.nav a{text-decoration:none;color:inherit;position:relative}
.nav a.active{color:var(--accent)}
.site-header .nav{left:850px;top:28px}
.site-header .nav a{margin-right:33px}

/* hero */
.hero-photo{position:absolute;left:0;top:516px;width:1200px;height:516px;background:linear-gradient(90deg,#dcdde0 0%,#eeeff1 40%,#f6f6f8 100%)}
.hero-bg{position:absolute;left:0;top:68px;width:1200px;height:585px}
.hero-kicker{position:absolute;left:0;width:1200px;top:284px;text-align:center;font-family:'Lato',Arial,sans-serif;font-weight:700;font-size:19px;color:var(--white)}
.hero-title{position:absolute;left:0;width:1200px;top:300px;text-align:center;font-family:'Lato',Arial,sans-serif;font-weight:400;font-size:45px;color:var(--white)}
.btn-solid{position:absolute;left:534px;top:371px;width:132px;height:37px;background:var(--accent);color:var(--white);font-size:11px;font-weight:500;display:flex;align-items:center;justify-content:center;text-transform:uppercase}

/* features */
.feature-title{position:absolute;font-family:'Lato',Arial,sans-serif;font-size:30px;color:var(--ink);font-weight:400}
.feature-text{position:absolute;width:463px;font-size:13px;line-height:24px;color:var(--ink)}
.btn-outline{position:absolute;border:1px solid #c9c9cf;background:var(--white);color:var(--ink);font-size:10.5px;display:flex;align-items:center;justify-content:center;text-transform:uppercase}
.land-photo{position:absolute;left:616px;top:1032px;width:584px;height:400px;background:linear-gradient(180deg,#c9dcef 0%,#a8bfd6 35%,#4a4f57 65%,#2b2e33 100%)}

/* pricing */
.section-title{position:absolute;left:0;width:1200px;top:1522px;text-align:center;font-family:'Lato',Arial,sans-serif;font-size:30px;font-weight:400;color:var(--ink)}
.section-sub{position:absolute;left:0;width:1200px;top:1578px;text-align:center;font-size:12.5px;line-height:20px;color:var(--text)}
.plan{position:absolute;top:1639px;width:334px;height:532px;background:var(--white);border:1px solid var(--line);border-radius:3px;overflow:hidden}
.plan-head{position:relative;height:240px;color:var(--white);text-align:center;border-bottom:3px solid}
.plan-standard .plan-head{background:var(--standard);border-color:var(--standard-dark)}
.plan-extended .plan-head{background:var(--extended);border-color:var(--extended-dark)}
.plan-premium .plan-head{background:var(--premium);border-color:var(--premium-dark)}
.plan-name{position:absolute;left:0;right:0;top:42px;font-size:26px;font-weight:400}
.plan-price{position:absolute;left:0;right:0;top:72px;font-size:68px;font-weight:500;line-height:1}
.plan-price sup{font-size:18px;vertical-align:top;position:relative;top:6px;margin-right:2px}
.plan-price small{font-size:15px;margin-left:2px}
.plan-note{position:absolute;left:0;right:0;top:156px;font-size:13px;font-weight:500;line-height:20px}
.ribbon{position:absolute;right:-34px;top:20px;width:140px;height:30px;background:var(--ribbon);transform:rotate(45deg);font-size:11px;font-weight:500;display:flex;align-items:center;justify-content:center;text-transform:uppercase}
.plan-body{position:absolute;left:41px;top:280px;width:270px}
.plan-body h3{font-family:'Lato',Arial,sans-serif;font-weight:400;font-size:22px;color:var(--ink)}
.plan-body .lead{font-size:11.5px;color:var(--ink);margin-top:2px}
.plan-body ul{list-style:none;margin-top:18px}
.plan-body li{position:relative;padding-left:23px;font-size:12px;line-height:20px;color:var(--text);margin-bottom:18px}
.plan-body li svg{position:absolute;left:0;top:4px}
.plan-body .btn-outline{position:relative;width:119px;height:35px;margin-top:-2px}

/* footer */
.site-footer{position:absolute;left:0;top:2265px;width:1200px;height:154px;background:var(--footer)}
.site-footer .brand{left:89px;top:46px;color:var(--white);font-size:22px}
.site-footer .nav{left:864px;top:52px;color:var(--white)}
.site-footer .nav a{margin-right:30px}
.footer-bar{position:absolute;left:850px;top:0;width:56px;height:3px;background:var(--accent)}
.footer-rule{position:absolute;left:89px;top:106px;width:1021px;height:1px;background:#33343a}
.copyright{position:absolute;left:0;width:1200px;top:125px;text-align:center;font-size:11px;font-weight:500;color:var(--white)}
.to-top{position:absolute;left:1142px;top:2247px;width:36px;height:36px;border-radius:50%;background:var(--accent);display:flex;align-items:center;justify-content:center;z-index:6}
</style>
</head>
<body>

<header class="site-header">
  <div class="brand">Logo Here</div>
  <nav class="nav">
    <a class="active" href="#">Home</a><a href="#">Service</a><a href="#">Contact</a><a href="#">Pricing</a>
  </nav>
</header>

<div class="hero-photo" role="img" aria-label="Photo of two colleagues working at a white desk with a laptop"></div>

<svg class="hero-bg" width="1200" height="585" viewBox="0 0 1200 585" role="img" aria-label="Deep blue backdrop with glowing particle waves">
  <defs>
    <radialGradient id="heroGlow" cx="0.5" cy="0.05" r="0.8">
      <stop offset="0" stop-color="#1a8ee0"/>
      <stop offset="0.45" stop-color="#0a4fae"/>
      <stop offset="1" stop-color="#062a6b"/>
    </radialGradient>
    <linearGradient id="edgeLeft" x1="0" x2="1">
      <stop offset="0" stop-color="#2fd6f0" stop-opacity="0.5"/>
      <stop offset="1" stop-color="#2fd6f0" stop-opacity="0"/>
    </linearGradient>
    <linearGradient id="edgeRight" x1="1" x2="0">
      <stop offset="0" stop-color="#2fd6f0" stop-opacity="0.5"/>
      <stop offset="1" stop-color="#2fd6f0" stop-opacity="0"/>
    </linearGradient>
    <clipPath id="heroShape">
      <polygon points="0,0 1200,0 1200,448 287,585 0,448"/>
    </clipPath>
  </defs>
  <g clip-path="url(#heroShape)">
    <rect x="0" y="0" width="1200" height="585" fill="url(#heroGlow)"/>
    <rect x="0" y="0" width="200" height="585" fill="url(#edgeLeft)"/>
    <rect x="1000" y="0" width="200" height="585" fill="url(#edgeRight)"/>
  </g>
</svg>

<p class="hero-kicker">Data , Analysis , Action</p>
<h1 class="hero-title">To keep your property Safe</h1>
<a class="btn-solid">Learn more</a>

<section>
  <h2 class="feature-title" style="left:647px;top:752px">Doc Secure</h2>
  <p class="feature-text" style="left:648px;top:802px">Lorem ipsum dolor sit amet, consectetuer adipiscing elit. Aenean commodo ligula eget dolor aenean massa. Cum sociis natoque penatibus et magnis dis parturient montes, nascetur ridiculus mus.</p>
  <a class="btn-outline" style="left:648px;top:898px;width:105px;height:34px">Read more</a>
</section>

<section>
  <h2 class="feature-title" style="left:87px;top:1191px">Land Secure</h2>
  <p class="feature-text" style="left:88px;top:1240px">Lorem ipsum dolor sit amet, consectetuer adipiscing elit. Aenean commodo ligula eget dolor aenean massa. Cum sociis natoque penatibus et magnis dis parturient montes, nascetur ridiculus mus.</p>
  <a class="btn-outline" style="left:88px;top:1335px;width:106px;height:35px">Read more</a>
  <div class="land-photo" role="img" aria-label="Photo of a modern house against a pale blue sky"></div>
</section>

<section>
  <h2 class="section-title">Pricing</h2>
  <p class="section-sub">Lorem ipsum dolor sit amet, consectetuer adipiscing elit. Aenean commodo ligula eget dolor.<br>Aenean massa. Cum sociis natoque penatibus et magnis</p>

  <article class="plan plan-standard" style="left:89px">
    <div class="plan-head">
      <div class="ribbon">Popular</div>
      <div class="plan-name">STANDARD</div>
      <div class="plan-price"><sup>$</sup>0</div>
      <div class="plan-note">1 user is free</div>
    </div>
    <div class="plan-body">
      <h3>Free includes</h3>
      <p class="lead">All of these great features:</p>
      <ul>
        <li><svg width="12" height="12" viewBox="0 0 12 12"><circle cx="6" cy="6" r="6" fill="#d04b7b"/><path d="M3.3 6.2l1.8 1.8 3.6-3.8" stroke="#fff" stroke-width="1.4" fill="none"/></svg>Lorem ipsum dolor sit amet, consectetuer adipiscing elit.</li>
        <li><svg width="12" height="12" viewBox="0 0 12 12"><circle cx="6" cy="6" r="6" fill="#d04b7b"/><path d="M3.3 6.2l1.8 1.8 3.6-3.8" stroke="#fff" stroke-width="1.4" fill="none"/></svg>Aenean commodo ligula eget dolor aenean massa. Cum sociis natoque penati.</li>
      </ul>
      <a class="btn-outline">Read more</a>
    </div>
  </article>

  <article class="plan plan-extended" style="left:432px">
    <div class="plan-head">
      <div class="plan-name">ENTENDED</div>
      <div class="plan-price"><sup>$</sup>6<small>67</small></div>
      <div class="plan-note">Per active User,Per month<br>billed annually</div>
    </div>
    <div class="plan-body">
      <h3>Standard includes</h3>
      <p class="lead">Everything in <b>Free</b>, and:</p>
      <ul>
        <li><svg width="12" height="12" viewBox="0 0 12 12"><circle cx="6" cy="6" r="6" fill="#3fb0c6"/><path d="M3.3 6.2l1.8 1.8 3.6-3.8" stroke="#fff" stroke-width="1.4" fill="none"/></svg>Lorem ipsum dolor sit amet, consectetuer adipiscing elit.</li>
        <li><svg width="12" height="12" viewBox="0 0 12 12"><circle cx="6" cy="6" r="6" fill="#3fb0c6"/><path d="M3.3 6.2l1.8 1.8 3.6-3.8" stroke="#fff" stroke-width="1.4" fill="none"/></svg>Aenean commodo ligula eget dolor aenean massa. Cum sociis natoque penati.</li>
      </ul>
      <a class="btn-outline">Read more</a>
    </div>
  </article>

  <article class="plan plan-premium" style="left:776px">
    <div class="plan-head">
      <div class="plan-name">PREMIUM</div>
      <div class="plan-price"><sup>$</sup>12</div>
      <div class="plan-note">Per active User,Per month<br>billed annually</div>
    </div>
    <div class="plan-body">
      <h3>Plus includes</h3>
      <p class="lead">Everything in <b>Standard</b>, and:</p>
      <ul>
        <li><svg width="12" height="12" viewBox="0 0 12 12"><circle cx="6" cy="6" r="6" fill="#5db59b"/><path d="M3.3 6.2l1.8 1.8 3.6-3.8" stroke="#fff" stroke-width="1.4" fill="none"/></svg>Lorem ipsum dolor sit amet, consectetuer adipiscing elit.</li>
        <li><svg width="12" height="12" viewBox="0 0 12 12"><circle cx="6" cy="6" r="6" fill="#5db59b"/><path d="M3.3 6.2l1.8 1.8 3.6-3.8" stroke="#fff" stroke-width="1.4" fill="none"/></svg>Aenean commodo ligula eget dolor aenean massa. Cum sociis natoque penati.</li>
      </ul>
      <a class="btn-outline">Read more</a>
    </div>
  </article>
</section>

<a class="to-top" aria-label="Back to top"><svg width="14" height="10" viewBox="0 0 14 10"><path d="M2 8l5-5 5 5" stroke="#fff" stroke-width="2" fill="none"/></svg></a>

<footer class="site-footer">
  <span class="footer-bar"></span>
  <div class="brand">Logo Here</div>
  <nav class="nav">
    <a class="active" href="#">Home</a><a href="#">Service</a><a href="#">Contact</a><a href="#">Pricing</a>
  </nav>
  <div class="footer-rule"></div>
  <p class="copyright">Copyright 2017 | All Right Reserved</p>
</footer>

</body>
</html>
```